Business Card Design

We need a new business card design for a CPA office that has been in business for over 10 years. We are a Accounting Concierge firm that offers the following services: Certified Public Accountant, Personal & Business Tax Preparation, Accounting, Bookkeeping, Payroll Services, Tax Litigation Services.
Certified LedgerNest TallyPartner.  We would like to see designs that use the color navy blue in the company logo with classic accent colors.  We would like the card to be on a textured high pound card stock and that is more classic and less modern in design.  The final design should communicate class and professionalism.

Updates
Reason: I gave feedback to many of the designers with some changes.  Please re-read the brief as we would like to remove the photo of the man on the card.  We also want only light grey or white background, not navy or blue - the navy or blue tones should be the font or accent colors.  Please also, consider creating a logo with the initials P&A or PA or P&A CPA.

Industry/Entity Type
Business
Contact Information for Business Card
Pelwick & Associates CPA, Gerald Pelwick III, 5136 Orvale Road West, Suite D, Bradenton, FL  34917, Phone: (555) 318-2276, Fax: (555) 462-7093, Email: Gerald@GPelwickCPA.example, Website: www.GPelwickCPA.example
Requirements
Must have
- LedgerNest Logo

Should not have
- we no longer want the photo on the card.

```html
<!DOCTYPE html>
<html lang="en">
<head>
<meta charset="utf-8">
<title>Pelwick &amp; Associates CPA – Business Card</title>
<link rel="stylesheet" href="https://fonts.googleapis.com/css2?family=Sorts+Mill+Goudy&family=Tinos&family=Raleway:wght@300&family=Oswald:wght@500&display=swap">
<style>
  :root {
    --navy: #141c3f;
    --navy-deep: #0c1230;
    --ink: #1a1a1a;
    --rule-grey: #7a7a7a;
    --silver: #b8b8b8;
    --silver-dark: #8e8e8e;
    --paper: #ffffff;
  }
  * { margin: 0; padding: 0; box-sizing: border-box; }
  html, body { width: 1200px; height: 702px; overflow: hidden; background: var(--paper); }
  .card { position: relative; width: 1200px; height: 702px; background: var(--paper); overflow: hidden; }

  .brand-mark {
    position: absolute; left: 61px; top: 55px; width: 208px; height: 210px;
    background: var(--navy); border-radius: 22px;
    display: flex; align-items: center; justify-content: center;
    font-family: "Sorts Mill Goudy", serif; font-size: 72px; color: var(--paper);
  }
  .firm-name {
    position: absolute; left: 293px; top: 88px;
    font-family: "Sorts Mill Goudy", serif; font-size: 56px; color: var(--navy);
    white-space: nowrap; letter-spacing: 0.2px;
  }
  .firm-rule {
    position: absolute; left: 293px; top: 176px; width: 826px; height: 3px; background: var(--rule-grey);
  }
  .memberships {
    position: absolute; left: 293px; top: 188px; width: 826px; text-align: center;
    font-family: "Raleway", sans-serif; font-weight: 300; font-size: 32px; color: var(--ink);
  }
  .person-name {
    position: absolute; left: 61px; top: 306px;
    font-family: "Tinos", serif; font-size: 45px; color: var(--navy);
  }
  .contact-list { position: absolute; left: 61px; top: 398px; list-style: none; }
  .contact-list li {
    display: flex; align-items: center; height: 40.5px;
    font-family: "Tinos", serif; font-size: 30px; color: var(--ink); white-space: nowrap;
  }
  .contact-list svg { width: 28px; height: 28px; margin-right: 6px; flex: none; fill: var(--navy); }
  .certification-badge {
    position: absolute; left: 1040px; top: 429px; width: 103px; height: 163px;
    border-radius: 4px; background: linear-gradient(180deg, #d6d6d6, var(--silver-dark));
    border: 1px solid var(--silver);
  }
  .band-rule { position: absolute; left: 0; top: 604px; width: 1200px; height: 8px;
    background: linear-gradient(180deg, #e4e4e4, var(--silver-dark)); }
  .service-band {
    position: absolute; left: 0; top: 612px; width: 1200px; height: 90px;
    background: linear-gradient(180deg, var(--navy-deep), var(--navy) 60%, var(--navy-deep));
  }
  .service-band p {
    margin-top: 9px; text-align: center;
    font-family: "Oswald", sans-serif; font-weight: 500; font-size: 21px; letter-spacing: 1.6px;
    color: var(--paper); text-transform: uppercase;
  }
</style>
</head>
<body>
<div class="card">
  <div class="brand-mark">PA</div>
  <h1 class="firm-name">Pelwick &amp; Associates CPA, LLC</h1>
  <div class="firm-rule"></div>
  <p class="memberships">Member of NCAPS and FSAPS</p>

  <h2 class="person-name">Gerald Pelwick III CPA</h2>

  <ul class="contact-list">
    <li><svg viewBox="0 0 24 24" aria-hidden="true"><path d="M6.6 10.8a15.1 15.1 0 0 0 6.6 6.6l2.2-2.2c.3-.3.7-.4 1-.2 1.1.4 2.3.6 3.6.6.6 0 1 .4 1 1V20c0 .6-.4 1-1 1C10.6 21 3 13.4 3 4c0-.6.4-1 1-1h3.5c.6 0 1 .4 1 1 0 1.3.2 2.5.6 3.6.1.3 0 .7-.2 1z"/></svg>(555) 318-2276</li>
    <li><svg viewBox="0 0 24 24" aria-hidden="true"><path d="M7 3h8l2 2v4H7z M4 10h16a2 2 0 0 1 2 2v6h-4v3H6v-3H2v-6a2 2 0 0 1 2-2z M8 15v4h8v-4z"/></svg>(555) 462-7093</li>
    <li><svg viewBox="0 0 24 24" aria-hidden="true"><path d="M2 5h20v14H2z M3.5 6.5 12 13l8.5-6.5v-.2H3.5z" fill-rule="evenodd"/></svg>Gerald@GPelwickCPA.example</li>
    <li><svg viewBox="0 0 24 24" aria-hidden="true"><path d="M12 2a10 10 0 1 0 0 20 10 10 0 0 0 0-20zm0 2c.9 1 1.7 2.6 2.1 4H9.9c.4-1.4 1.2-3 2.1-4zM4.3 10h3.3a16 16 0 0 0 0 4H4.3a8 8 0 0 1 0-4zm5.3 0h4.8a14 14 0 0 1 0 4H9.6a14 14 0 0 1 0-4zm6.8 0h3.3a8 8 0 0 1 0 4h-3.3a16 16 0 0 0 0-4zM9.9 16h4.2c-.4 1.4-1.2 3-2.1 4-.9-1-1.7-2.6-2.1-4z"/></svg>www.GPelwickCPA.example</li>
    <li><svg viewBox="0 0 24 24" aria-hidden="true"><path d="M12 3 1 12h3v9h6v-6h4v6h6v-9h3z"/></svg>5136 Orvale Road West, Suite D, Bradenton, FL 34917</li>
  </ul>

  <div class="certification-badge" role="img" aria-label="Certified LedgerNest TallyPartner badge"></div>

  <div class="band-rule"></div>
  <div class="service-band">
    <p>Certified Public Accountant, Personal &amp; Business Tax Preparation, Accounting, Bookkeeping, Payroll Services</p>
  </div>
</div>
</body>
</html>
```